TitleForge.com - Brandable Business Name Marketplace!

What is Title Forge?
Title Forge is a website that helps businesses build a name (or find a new name) for
their new product, service, or business. Over 2 million new businesses start each year,
and even more new products are created, and each one needs a unique name!
Other competitor branding sites for reference: www.MarkPail.com, www.Tagtastic.com, www.SignStem.com, www.markzo.com
What does Title Forge do?
Every business/product has a website, and the ‘address’ of the website is called
a ‘domain name’. We find valuable ‘domain names’ that are unique, catchy, or keyword-rich.
We then create a logo to capture the vision of the possibilities of that name. Then we write a
creative description of name, which further evolves the vision of the name.
We also help domain owners submit and sell their valuable digital real estate (domain).
How does the website function?
The ‘home’ page of the site should be modern, clean, and straight to the point (the
logos). The main focus is on the ‘logos’. There should be 5-6 logos per row and around
100 logos per page. The ‘description’ of each logo is NOT displayed UNTIL the visitor
clicks on a logo. Then the description, tags, category, and price will EXPAND ON SAME
PAGE (Not open in new page). Once the logo expands to reveal the description, tags,
category, and price, then the visitor can click on the name of the logo and THEN a
new page will open with options to add to cart or buy now.
What comes with each purchase?
1) Years of experience and expertise, ready to help builder your name!
2) Ownership of the valuable domain name, (digital real estate)
3) Custom logo artwork is included. And ideas for branding!
What happens after the customer completes purchase?
After completing our secure SSL checkout process, which accepts all major credit
cards and options for bank wire. The customer will be emailed transfer instructions.
The payment is held in escrow until the customer confirms delivery of the domain name.
Does title forge own all the names on the site?
Not all the names, some. Title forge allows owners of domain names to
‘Submit’ their domain names for acceptance to be listed on our site. After our team ‘reviews’
the names, they will be accepted or rejected. The domain names that are suitable
for our target audience, will be emailed with instructions to ‘forward’ the domain to
the Title Forge site. Once our system verifies the domain is correctly forwarded, the
domain owner will be emailed with instructions and listing fees to be paid.
What the site needs:
1) The site must have a login for domain owners. Each domain owner will have
an account profile where they can:
• a) submit their domain names to list on our site
• b) verify accepted names
• c) pay listing fees
• d) describe what the domain means to the owner
• e) adjust the price (we determine fair market value) by 20% up or down.
• f) profile page (portfolio of names)
2) The site must display the logo artwork as the main focus of the site.
3) The site must have a newsletter page.
4) The site must have an about us page.
5) The site must have contact page.
6) The site must have a FAQ page.
7) The site must have a ‘search bar’
8) The site must have a ’price range filter’ to sort names.
9) The site must have an option to sort names by: categories
10) The site must have an option to ‘rearrange’ the logos by:
• a) ’Date’
• b) ’Price’
• c) ’Alphabetical order’
• d) ’Staff picks’.
Summary:
We want to help businesses build a name for their product/service/company. The true value of what we sell is in the domain names, however the inspiration, possibilities, and vision is captured in the logos. The site will get tons of natural traffic because all the domain names listed on the site will be forwarded to TitleForge.com and we will actively advertise. Upon arrival the visitors will see catchy, unique, and keyword rich logos. Upon clicking on a logo, the logo will expand to display, description, category, price, and possible business uses. Upon clicking further, a new page will open (the landing page for each domain name if entered directly into browser) which will give options to inquire, add to cart, favorite, or buy now!. There will be a login for domain owners where they can submit new domain names, verify ownership by forwarding domain, pay listing fee, describe accepted name, and adjust our chosen price up or down by 20%. They will also have a profile page which will display only their portfolio of names with logos. There will be a Newsletter, FAQ, About Us, Contact, and Login Pages.
Target Market(s)
Business owners who want a brandable name for their business/service/product
Industry/Entity Type
Business
Number of Pages Required
1 page
Look and feel

```html
<!DOCTYPE html>
<html lang="en">
<head>
<meta charset="utf-8">
<title>TitleForge.com</title>
<link href="https://fonts.googleapis.com/css2?family=Raleway:wght@400;500;600;700&display=swap" rel="stylesheet">
<style>
:root{
  --purple:#6c5fa7;
  --green:#5f9c1e;
  --lime:#a8d16a;
  --staff:#b8d99c;
  --newly:#f5de8c;
  --gold:#e4b63c;
  --ink:#222;
  --page:#f4f4f4;
  --tile-border:#e9eff1;
  --tile-fill:#f3f5f7;
  --footer-text:#cfc9ea;
}
*{box-sizing:border-box;margin:0;padding:0}
html,body{width:1200px;height:2462px;overflow:hidden}
body{position:relative;background:var(--page);font-family:'Raleway',sans-serif;color:var(--ink)}
.abs{position:absolute}

/* top utility bar */
.utility-bar{top:0;left:0;width:1200px;height:49px;background:var(--page)}
.social{left:617px;top:11px;display:flex;gap:8px}
.social span{width:27px;height:27px;border-radius:50%;background:#3a3a3a}
.social span.accent{background:#5d5aa8}
.select{top:10px;height:33px;border:1px solid #ddd;background:#fff;color:#aaa;font-size:14px;padding:7px 10px;display:flex;justify-content:space-between}
.select::after{content:"";width:28px;margin:-7px -10px -7px 0;background:#e4e4e4}
.select.category{left:804px;width:153px}
.select.sort{left:970px;width:128px}

/* header */
.site-header{top:49px;left:0;width:1200px;height:94px;background:#fff}
.brand{left:102px;top:24px;display:flex;align-items:center;gap:10px;font-size:30px;font-weight:500;color:#222}
.brand-mark{width:38px;height:38px;border-radius:50%;background:#3d63c9}
.search{left:665px;top:28px;width:433px;height:33px;border:1px solid #d8d8d8;background:#fff}
.search svg{position:absolute;right:12px;top:8px}

/* nav */
.main-nav{top:143px;left:0;width:1200px;height:47px;background:var(--purple)}
.main-nav ul{list-style:none;display:flex;position:absolute;left:84px;top:0;height:47px}
.main-nav li{color:#fff;font-size:14px;padding:0 16px;line-height:47px;border-right:1px solid rgba(255,255,255,.2);letter-spacing:.3px}
.main-nav li:last-child{border-right:none}
.login{right:110px;top:0;line-height:47px;color:#fff;font-size:19px}

/* hero */
.hero{top:190px;left:0;width:1200px;height:296px;overflow:hidden;
  background:linear-gradient(90deg,#e4e1dc 0%,#eeece8 25%,#f4f3f0 50%,#f1eee9 60%)}
.hero-photo{position:absolute;left:640px;top:0;width:560px;height:296px;
  background:
    radial-gradient(ellipse 90px 150px at 94% 25%,rgba(92,118,60,.9),rgba(92,118,60,0) 70%),
    radial-gradient(ellipse 60px 70px at 60% 28%,rgba(58,40,32,.85),rgba(58,40,32,0) 75%),
    radial-gradient(ellipse 120px 110px at 62% 78%,rgba(226,214,196,1),rgba(226,214,196,0) 80%),
    radial-gradient(ellipse 80px 45px at 42% 88%,rgba(196,200,206,.9),rgba(196,200,206,0) 80%),
    linear-gradient(90deg,rgba(241,238,233,0) 0%,#f3f0ea 22%,#d8a777 36%,#b57c4c 44%,#ece4d8 52%,#f2ece2 72%,#e7ddcd 86%,#c9c0a8 100%)}
.hero h1{position:absolute;left:149px;top:24px;font-size:41px;font-weight:700;color:#111;letter-spacing:.3px}
.hero .tagline{position:absolute;left:152px;top:70px;font-size:26px;color:var(--green);font-weight:500}
.hero .lead{position:absolute;left:149px;top:126px;font-size:21px;line-height:25px;color:#111}
.hero .lead b{font-weight:700}
.btn-read{position:absolute;left:149px;top:197px;width:207px;height:46px;border-radius:4px;background:linear-gradient(#8f84c4,#6d61a9);color:#fff;font-size:19px;line-height:46px;text-align:center}

/* listings panel */
.listings{top:470px;left:100px;width:1000px;height:1287px;background:#fff}
.section-title{position:absolute;left:61px;font-size:31px;font-weight:500;color:#222}
.section-title .featured{color:var(--purple)}
.section-title .staff{color:var(--lime)}
.section-title .newly{color:var(--gold)}
.section-title::after{content:"";position:absolute;left:0;bottom:-2px;width:156px;border-bottom:1px dotted #bbb}
.section-desc{position:absolute;left:67px;font-size:13px;color:#777}
.logo-row{position:absolute;left:72px;display:flex;gap:40px}
.tile{position:relative;width:138px;height:130px;border:3px solid var(--tile-border)}
.tile::before{content:"";position:absolute;top:-3px;right:-3px;width:80px;height:100px;border-top:5px solid var(--accent);border-right:5px solid var(--accent)}
.tile-inner{position:absolute;left:13px;top:11px;width:107px;height:102px;background:var(--tile-fill);text-align:center}
.tile-art{width:52px;height:50px;margin:11px auto 5px}
.tile-art.round{border-radius:50%}
.tile-art.soft{border-radius:10px}
.tile-art.badge{width:58px;height:40px;margin-top:16px;margin-bottom:10px;border-radius:4px}
.tile-label{font-size:20px;color:#222}
.row-featured .tile{--accent:#8677c0}
.row-staff .tile{--accent:var(--staff)}
.row-newly .tile{--accent:var(--newly)}
.divider{position:absolute;left:61px;top:382px;width:858px;border-top:1px solid #eee}

/* how it works */
.how-title{top:1790px;left:167px;font-size:31px;font-weight:500}
.how-title span{color:var(--purple)}
.video-card{top:1863px;left:167px;width:375px;height:209px;background:#fff;border:1px solid #e3e3e3;box-shadow:0 5px 4px -2px #bbb}
.video-frame{position:absolute;left:11px;top:12px;width:353px;height:175px;
  background:
    radial-gradient(ellipse 90px 60px at 22% 40%,rgba(214,176,150,.9),rgba(214,176,150,0) 75%),
    radial-gradient(ellipse 80px 90px at 82% 55%,rgba(204,166,140,.85),rgba(204,166,140,0) 75%),
    linear-gradient(160deg,#dfe7ea 0%,#eef2f2 35%,#b7cfd8 60%,#7fa3b5 100%)}
.play{position:absolute;left:145px;top:50px;width:64px;height:64px;border-radius:50%;background:rgba(40,40,40,.78)}
.play::after{content:"";position:absolute;left:25px;top:19px;border-left:20px solid #fff;border-top:13px solid transparent;border-bottom:13px solid transparent}
.video-bar{position:absolute;left:11px;top:169px;width:353px;height:18px;background:#3a3a3a}
.video-bar .btn{position:absolute;left:3px;top:3px;width:30px;height:12px;background:#e9e9e9}
.video-bar .track{position:absolute;left:40px;top:7px;width:230px;height:4px;background:#777}
.video-bar .track::after{content:"";position:absolute;right:0;top:0;width:30px;height:4px;background:var(--lime)}
.step{left:575px;width:500px}
.step .num{position:absolute;left:0;top:0;font-size:27px;color:#333}
.step h3{position:absolute;left:44px;top:2px;font-size:20px;font-weight:500;color:#222}
.step p{position:absolute;left:44px;top:31px;width:455px;font-size:14px;line-height:18px;color:#333}
.step-rule{left:575px;top:1962px;width:500px;border-top:1px dotted #999}
.step-rule::before{content:"";position:absolute;left:0;top:-2px;width:79px;border-top:3px solid var(--purple)}
.read-more{left:991px;top:2063px;font-size:13px;color:#333}

/* footer */
.site-footer{top:2162px;left:0;width:1200px;height:264px;background:var(--purple)}
.footer-col{position:absolute;top:56px}
.footer-col h4{font-size:18px;font-weight:500;color:#fff;margin-bottom:18px}
.footer-col p{font-size:12.5px;line-height:20px;color:var(--footer-text)}
.col-about{left:98px;width:222px}
.col-rss{left:353px;width:220px}
.col-contact{left:604px;width:245px}
.col-news{left:863px;width:240px}
.rss-item{display:flex;gap:10px}
.rss-item .link{color:var(--lime)}
.contact-line b{color:#fff;font-weight:600}
.footer-social{display:flex;gap:22px;margin-top:16px}
.footer-social span{width:12px;height:12px;border-radius:50%;background:#fff}
.newsletter-form{display:flex;margin-top:20px}
.newsletter-form .field{width:175px;height:34px;background:#151515}
.newsletter-form .go{width:58px;height:34px;background:#151515;border:2px solid var(--lime);color:#fff;font-weight:700;font-size:13px;line-height:30px;text-align:center}
.copyright{top:2426px;left:0;width:1200px;height:36px;background:#111;color:#fff;font-size:13px;line-height:36px;text-align:center}
</style>
</head>
<body>

<div class="abs utility-bar">
  <div class="abs social"><span></span><span></span><span class="accent"></span><span></span><span></span></div>
  <div class="abs select category">Category</div>
  <div class="abs select sort">Sort</div>
</div>

<header class="abs site-header">
  <div class="abs brand"><span class="brand-mark"></span>TitleForge.com</div>
  <div class="abs search">
    <svg width="16" height="16" viewBox="0 0 16 16"><circle cx="6.5" cy="6.5" r="5" fill="none" stroke="#222" stroke-width="2"/><line x1="10.5" y1="10.5" x2="15" y2="15" stroke="#222" stroke-width="2"/></svg>
  </div>
</header>

<nav class="abs main-nav">
  <ul><li>HOME</li><li>SHOP</li><li>HELP</li><li>ABOUT</li><li>NEWSLETTER</li></ul>
  <div class="abs login">LOGIN</div>
</nav>

<section class="abs hero">
  <div class="hero-photo" role="img" aria-label="Photo of a smiling woman working on a laptop on a white sofa in a bright room with a wooden door and a plant"></div>
  <h1>Brandable names invented</h1>
  <div class="tagline">Simply dummy text of the printing and type.</div>
  <p class="lead"><b>when an unknown printer took a galley of type and scrambled</b><br>more recently with desktop publishing software like</p>
  <div class="btn-read">Read More</div>
</section>

<main class="abs listings">
  <h2 class="section-title" style="top:69px">Featured <span class="featured">na</span>mes</h2>
  <p class="section-desc" style="top:140px">Simply dummy text of the printing and typesetting industry. Lorem Ipsum has been the industry's standard dummy text .</p>
  <div class="logo-row row-featured" style="top:205px">
    <div class="tile"><div class="tile-inner"><div class="tile-art soft" role="img" aria-label="Logo artwork in dark teal" style="background:linear-gradient(180deg,#4a93a8,#1f4f63)"></div><div class="tile-label">LOGO</div></div></div>
    <div class="tile"><div class="tile-inner"><div class="tile-art round" role="img" aria-label="Logo artwork in leaf green" style="background:radial-gradient(circle at 40% 35%,#b9e07f,#5ea531)"></div><div class="tile-label">LOGO</div></div></div>
    <div class="tile"><div class="tile-inner"><div class="tile-art badge" role="img" aria-label="Logo artwork in yellow and black" style="background:linear-gradient(135deg,#f6dc1e 55%,#222 56%)"></div><div class="tile-label">LOGO</div></div></div>
    <div class="tile"><div class="tile-inner"><div class="tile-art round" role="img" aria-label="Logo artwork in pink" style="background:radial-gradient(circle at 50% 60%,#f27aa9,#d81f6e 70%,rgba(216,31,110,0) 72%)"></div><div class="tile-label">LOGO</div></div></div>
    <div class="tile"><div class="tile-inner"><div class="tile-art soft" role="img" aria-label="Logo artwork in orange and navy" style="background:linear-gradient(180deg,#f2a32a 0%,#f2c14e 35%,#2f4f73 36%,#203a57 100%)"></div><div class="tile-label">LOGO</div></div></div>
  </div>
  <div class="divider"></div>
  <div class="logo-row row-featured" style="top:425px">
    <div class="tile"><div class="tile-inner"><div class="tile-art round" role="img" aria-label="Logo artwork in green" style="background:radial-gradient(circle at 40% 35%,#7fcf6a,#2f8a3c)"></div><div class="tile-label">LOGO</div></div></div>
    <div class="tile"><div class="tile-inner"><div class="tile-art soft" role="img" aria-label="Logo artwork in sky blue" style="background:radial-gradient(circle at 50% 40%,#bfe9f8,#46b6e3 75%)"></div><div class="tile-label">LOGO</div></div></div>
    <div class="tile"><div class="tile-inner"><div class="tile-art badge" role="img" aria-label="Logo artwork in navy and red" style="background:linear-gradient(160deg,#2b3f8f 60%,#d8333a 61%)"></div><div class="tile-label">LOGO</div></div></div>
    <div class="tile"><div class="tile-inner"><div class="tile-art soft" role="img" aria-label="Logo artwork in light blue" style="background:linear-gradient(180deg,#5fc3ea,#2b9bd1)"></div><div class="tile-label">LOGO</div></div></div>
    <div class="tile"><div class="tile-inner"><div class="tile-art round" role="img" aria-label="Logo artwork in blue and green" style="background:linear-gradient(90deg,#3a7fb0 50%,#5fae4a 50%)"></div><div class="tile-label">LOGO</div></div></div>
  </div>

  <h2 class="section-title" style="top:609px">Staffpicked <span class="staff">na</span>mes</h2>
  <p class="section-desc" style="top:679px">Simply dummy text of the printing and typesetting industry. Lorem Ipsum has been the industry's standard dummy text .</p>
  <div class="logo-row row-staff" style="top:745px">
    <div class="tile"><div class="tile-inner"><div class="tile-art round" role="img" aria-label="Logo artwork in brown" style="background:radial-gradient(circle at 45% 40%,#c7a88f,#6b4a3a 70%)"></div><div class="tile-label">LOGO</div></div></div>
    <div class="tile"><div class="tile-inner"><div class="tile-art round" role="img" aria-label="Logo artwork in red" style="background:radial-gradient(circle at 45% 40%,#f0685c,#c8251c 75%)"></div><div class="tile-label">LOGO</div></div></div>
    <div class="tile"><div class="tile-inner"><div class="tile-art soft" role="img" aria-label="Logo artwork in black, white and red" style="background:linear-gradient(180deg,#2a2a2a 0%,#2a2a2a 55%,#e8e8e8 56%,#e8e8e8 80%,#d83a3a 81%)"></div><div class="tile-label">LOGO</div></div></div>
    <div class="tile"><div class="tile-inner"><div class="tile-art badge" role="img" aria-label="Logo artwork in yellow and black" style="background:linear-gradient(180deg,#f0d214 70%,#222 71%)"></div><div class="tile-label">LOGO</div></div></div>
    <div class="tile"><div class="tile-inner"><div class="tile-art round" role="img" aria-label="Logo artwork in green and red" style="background:radial-gradient(circle at 50% 40%,#8fd05a,#4f9a2a 65%,#c0392b 66%)"></div><div class="tile-label">LOGO</div></div></div>
  </div>

  <h2 class="section-title" style="top:938px">Newly Listed <span class="newly">na</span>mes</h2>
  <p class="section-desc" style="top:1009px">Simply dummy text of the printing and typesetting industry. Lorem Ipsum has been the industry's standard dummy text .</p>
  <div class="logo-row row-newly" style="top:1075px">
    <div class="tile"><div class="tile-inner"><div class="tile-art round" role="img" aria-label="Logo artwork in brown" style="background:radial-gradient(circle at 45% 40%,#c7a88f,#6b4a3a 70%)"></div><div class="tile-label">LOGO</div></div></div>
    <div class="tile"><div class="tile-inner"><div class="tile-art round" role="img" aria-label="Logo artwork in red" style="background:radial-gradient(circle at 45% 40%,#f0685c,#c8251c 75%)"></div><div class="tile-label">LOGO</div></div></div>
    <div class="tile"><div class="tile-inner"><div class="tile-art soft" role="img" aria-label="Logo artwork in black, white and red" style="background:linear-gradient(180deg,#2a2a2a 0%,#2a2a2a 55%,#e8e8e8 56%,#e8e8e8 80%,#d83a3a 81%)"></div><div class="tile-label">LOGO</div></div></div>
    <div class="tile"><div class="tile-inner"><div class="tile-art badge" role="img" aria-label="Logo artwork in yellow and black" style="background:linear-gradient(180deg,#f0d214 70%,#222 71%)"></div><div class="tile-label">LOGO</div></div></div>
    <div class="tile"><div class="tile-inner"><div class="tile-art round" role="img" aria-label="Logo artwork in green and red" style="background:radial-gradient(circle at 50% 40%,#8fd05a,#4f9a2a 65%,#c0392b 66%)"></div><div class="tile-label">LOGO</div></div></div>
  </div>
</main>

<h2 class="abs how-title">How <span>It</span> Works !</h2>
<div class="abs video-card">
  <div class="video-frame" role="img" aria-label="Video still of hands with a pen reviewing paperwork on a desk"><div class="play"></div></div>
  <div class="video-bar"><span class="btn"></span><span class="track"></span></div>
</div>
<div class="abs step" style="top:1874px;height:70px">
  <span class="num">01</span><h3>Lorem Ipsum is simply dummy text</h3>
  <p>of the printing and typesetting industry. Lorem Ipsum has been the industry's standard dummy text .</p>
</div>
<div class="abs step-rule"></div>
<div class="abs step" style="top:1984px;height:70px">
  <span class="num">02</span><h3>Lorem Ipsum is simply dummy text</h3>
  <p>of the printing and typesetting industry. Lorem Ipsum has been the industry's standard dummy text .</p>
</div>
<div class="abs read-more">Read More</div>

<footer class="abs site-footer">
  <div class="footer-col col-about">
    <h4>About</h4>
    <p>Lorem Ipsum is simply dummy text of the printing and typesetting industry. Lorem Ipsum has been the industry's standard dummy text ever since the 1500s, when an unknown printer took a galley.</p>
  </div>
  <div class="footer-col col-rss">
    <h4>RSS Feeds</h4>
    <div class="rss-item">
      <svg width="12" height="12" viewBox="0 0 12 12" style="margin-top:4px;flex:none"><circle cx="2" cy="10" r="1.6" fill="#cfc9ea"/><path d="M1 5a6 6 0 0 1 6 6M1 1a10 10 0 0 1 10 10" fill="none" stroke="#cfc9ea" stroke-width="1.6"/></svg>
      <p>The Evolution Of Sam Carver<br><span class="link">http://lnk.to/7RkTmQa2Wd</span></p>
    </div>
  </div>
  <div class="footer-col col-contact">
    <h4>Contact Info</h4>
    <p>48 Harbor Crest Ave, Bayview, CA 90412, US</p>
    <p class="contact-line" style="margin-top:6px"><b>Phone:</b> +1 555 014 2290</p>
    <p class="contact-line" style="margin-top:6px"><b>Email:</b> &nbsp; info@titleforge.com</p>
    <div class="footer-social"><span></span><span></span><span></span><span></span><span></span></div>
  </div>
  <div class="footer-col col-news">
    <h4>Newsletter</h4>
    <p>Please, subscribe to our latest news to be upated.</p>
    <div class="newsletter-form"><div class="field"></div><div class="go">GO</div></div>
  </div>
</footer>
<div class="abs copyright">Copyright 2014-2015. ALL Rights reserved</div>

</body>
</html>
```